TorvaMax needs app design - Social app for a party on a budget

We need a design for our app called "TorvaMax", TorvaMax is an essential application that showcases the finest clubs in the city. The primary objective of the app is to provide users with insights into club ratings and beer prices, enabling them to locate the most cost-effective beer near their current location. You as a user will also have ability to rate different Additionally, users can view posts and images from various patrons, offering glimpses into the ambiance of the establishments to determine if they meet their preferences and requirements.

We imagine Torvamax having a "gamification app desigin" as partying is like a game, you experience new adventures and take on new quests.
Allthough we are open for different designs, surprise us.

Keyfeatures:
1 - Splash/Login Page:
Allow users to log in or sign up using Plimbo, Snapvera, or Chatterloo credentials.
2 - Home Page/Announcements:
Display user-generated posts from different clubs and pubs, showcasing crowd levels and overall enjoyment.
Enable users to like posts, with sorting based on likes and proximity.
Access announcements from establishments about upcoming events, entrance fees, and performances.
3 - Search Page:
Provide a map displaying nearby pubs and clubs, with basic information such as rating, beer prices, and operating hours.
4 - List Page:
Present a comprehensive list of nearby clubs and pubs, sorted initially by rating.
Allow users to sort by beer prices, location, and other criteria.
Enable users to rate establishments using a 1-5 star system, with monthly winners prominently featured on the announcement page.
5 - My page:
Allow users to revisit and upload memories, including pictures, locations, dates, and times.
Provide an option to repost pictures on Snapvera.
Feature a "Refer a Friend" button for users to earn complimentary memberships by referring friends who complete the registration process.

As mentioned these are only key features we imagine this app should have, feel free to play around with the design.

18

• Key features meantioned in project description

```html
<!DOCTYPE html>
<html lang="en">
<head>
<meta charset="utf-8">
<title>TorvaMax – App Screens</title>
<link href="https://fonts.googleapis.com/css2?family=Lato:wght@300;400;700;900&display=swap" rel="stylesheet">
<style>
:root{
  --canvas:#000;
  --screen:#0a0a0a;
  --bar:#ffffff;
  --text:#ffffff;
  --muted:#8a8a8a;
  --dim:#5a5a5a;
  --ink:#111111;
  --star:#ffd400;
  --field:#ffffff;
  --btn-grey:#a9a9a9;
}
*{box-sizing:border-box;margin:0;padding:0}
html,body{width:813px;height:1200px;overflow:hidden;background:var(--canvas)}
body{position:relative;font-family:'Lato',sans-serif;color:var(--text)}
.abs{position:absolute}
.phone{position:absolute;width:174px;height:377px;border-radius:14px;background:var(--screen);overflow:hidden}
.col1{left:130px}.col2{left:320px}.col3{left:509px}
.row1{top:19px}.row2{top:412px}.row3{top:804px}

.status{position:absolute;left:0;top:0;width:100%;height:26px;background:var(--bar);color:var(--ink);z-index:5}
.status .time{position:absolute;left:24px;top:8px;font-size:8px;font-weight:700}
.status svg{position:absolute;right:14px;top:9px}

.nav{position:absolute;left:0;bottom:0;width:100%;height:31px;background:var(--bar);z-index:5}
.nav svg{position:absolute;top:6px;width:10px;height:10px;stroke:#9a9a9a;fill:none;stroke-width:1.6}
.nav svg.active{stroke:var(--ink)}
.nav .n1{left:29px}.nav .n2{left:63px}.nav .n3{left:99px}.nav .n4{left:134px}
.nav .marker{position:absolute;top:0;width:12px;height:2px;background:var(--ink);border-radius:0 0 2px 2px}
.home-ind{position:absolute;left:57px;bottom:5px;width:61px;height:2px;border-radius:2px;background:var(--ink);z-index:6}
.home-ind.light{background:#fff}

.photo{position:absolute}
.ph-crowd{background:radial-gradient(circle at 40% 12%,#8aa3c9 0%,#3a4a78 18%,#1b1a33 40%,#2a1428 65%,#4a1838 100%)}
.ph-warm{background:linear-gradient(135deg,#c0396b 0%,#e0873a 40%,#6b2b3a 75%,#2a1418 100%)}
.ph-green{background:linear-gradient(160deg,#0b1a14 0%,#1d5a45 55%,#0a1a12 100%)}
.ph-neon{background:linear-gradient(180deg,#1a0608 0%,#7a1016 25%,#2a0d3a 55%,#120a18 100%)}
.ph-copper{background:linear-gradient(150deg,#d9b7a0 0%,#6b3a2a 50%,#2a1510 100%)}
.ph-map{background:linear-gradient(135deg,#e8ecef 0%,#dfe6ea 55%,#a8cbe8 78%,#8dbde6 100%)}
.avatar{background:linear-gradient(135deg,#cfc7c0,#6e625a)}

.logo{font-weight:900;letter-spacing:.5px;color:#fff}
.stars{position:absolute;right:9px;color:var(--star);font-size:6.5px;letter-spacing:.6px}
.title{position:absolute;left:9px;font-size:11px;font-weight:700}
.small{font-size:5.5px}
.body{font-size:7.5px}

/* sign up */
.label{position:absolute;left:9px;font-size:7px}
.field{position:absolute;left:9px;width:156px;height:18px;border:1px solid #d0d0d0;border-radius:3px}
.btn{position:absolute;background:#fff;color:var(--ink);border-radius:3px;font-size:5.5px;font-weight:700;display:flex;align-items:center;justify-content:center}

/* announcements */
.tabs{position:absolute;top:33px;width:100%;text-align:center;font-size:7.5px}
.tabs span{margin:0 6px}
.tabs .on{font-weight:700;color:#fff}
.tabs .off{color:var(--dim)}
.feed{position:absolute;top:62px;left:9px;width:158px}
.post h3{font-size:11px;font-weight:700;line-height:12px}
.post .date{font-size:6.5px;color:var(--dim);font-weight:300;margin-bottom:6px}
.post p{font-size:7.3px;line-height:8.8px;margin-bottom:8px}
.divider{width:26px;height:1px;background:#444;margin:6px auto 16px}

.row-info{position:absolute;left:9px;right:9px;font-size:7.3px;display:flex;justify-content:space-between}
.info{position:absolute;left:9px;font-size:7.3px;line-height:10.5px}
.loc{position:absolute;left:9px;font-size:5.5px;display:flex;align-items:center;gap:3px;color:#ddd}
.loc svg{width:6px;height:6px;stroke:#ddd;fill:none;stroke-width:1.5}
.search{position:absolute;left:9px;top:31px;font-size:5.5px;display:flex;align-items:center;gap:4px}
.search svg{width:8px;height:8px;stroke:#fff;fill:none;stroke-width:1.8}

.comment{position:absolute;left:9px;width:156px;height:23px;background:#fff;border-radius:2px;color:var(--ink)}
.comment .avatar{position:absolute;left:4px;top:5px;width:13px;height:13px;border-radius:50%}
.comment .who{position:absolute;left:21px;top:5px;font-size:5.5px}
.comment .who b{display:block;font-weight:400}
.comment .who i{font-style:normal;color:var(--star);font-size:4px;letter-spacing:.3px}
.comment .quote{position:absolute;left:51px;top:5px;width:100px;font-size:3.6px;line-height:4.6px}

.mem-meta{position:absolute;left:9px;font-size:5.5px;line-height:10px;color:#ddd}
.mem-meta div{display:flex;align-items:center;gap:3px}
.mem-meta svg{width:6px;height:6px;stroke:#ddd;fill:none;stroke-width:1.5}
.share{position:absolute;right:9px;display:flex;gap:5px}
.share span{width:6px;height:6px;border:1px solid #ddd;border-radius:50%}
.cam{position:absolute;right:9px;width:11px;height:9px;stroke:#fff;fill:none;stroke-width:1.5}
</style>
</head>
<body>

<svg width="0" height="0" style="position:absolute">
  <defs>
    <symbol id="i-home" viewBox="0 0 24 24"><path d="M3 10.5 12 3l9 7.5V21h-6v-6H9v6H3z"/></symbol>
    <symbol id="i-pin" viewBox="0 0 24 24"><path d="M12 22s-7-7.2-7-12.2A7 7 0 0 1 19 9.8C19 14.8 12 22 12 22z"/><circle cx="12" cy="10" r="2.6"/></symbol>
    <symbol id="i-list" viewBox="0 0 24 24"><path d="M8 5h13M8 12h13M8 19h13M3 5h1M3 12h1M3 19h1"/></symbol>
    <symbol id="i-user" viewBox="0 0 24 24"><circle cx="12" cy="8" r="4.5"/><path d="M3.5 22a8.5 8.5 0 0 1 17 0"/></symbol>
    <symbol id="i-search" viewBox="0 0 24 24"><circle cx="10.5" cy="10.5" r="7.5"/><path d="M16 16l6 6"/></symbol>
    <symbol id="i-cal" viewBox="0 0 24 24"><rect x="3" y="5" width="18" height="16" rx="2"/><path d="M3 10h18M8 3v4M16 3v4"/></symbol>
    <symbol id="i-clock" viewBox="0 0 24 24"><circle cx="12" cy="12" r="9"/><path d="M12 7v5l3 2"/></symbol>
    <symbol id="i-cam" viewBox="0 0 24 20"><path d="M2 6h5l2-3h6l2 3h5v12H2z"/><circle cx="12" cy="11.5" r="4"/></symbol>
    <symbol id="i-status" viewBox="0 0 36 8"><rect x="0" y="5" width="1.6" height="3"/><rect x="2.4" y="3.5" width="1.6" height="4.5"/><rect x="4.8" y="2" width="1.6" height="6"/><rect x="7.2" y="0.5" width="1.6" height="7.5"/><path d="M12.5 3.2a5 5 0 0 1 7 0l-1 1a3.6 3.6 0 0 0-5 0zM14.5 5.2a2.2 2.2 0 0 1 3 0L16 7z"/><rect x="24" y="1" width="10" height="6" rx="1.5"/><rect x="34.5" y="3" width="1" height="2"/></symbol>
  </defs>
</svg>

<!-- 1 Splash -->
<section class="phone col1 row1">
  <div class="status"><span class="time">9:41</span><svg width="32" height="7" fill="#111"><use href="#i-status"/></svg></div>
  <div class="photo ph-crowd" role="img" aria-label="Blurred crowd dancing under club stage lights" style="left:0;top:26px;width:174px;height:351px"></div>
  <div class="abs logo" style="top:176px;width:100%;text-align:center;font-size:20px">TorvaMax</div>
</section>

<!-- 2 Welcome -->
<section class="phone col2 row1">
  <div class="status"><span class="time">9:41</span><svg width="32" height="7" fill="#111"><use href="#i-status"/></svg></div>
  <div class="photo ph-crowd" role="img" aria-label="Blurred crowd dancing under club stage lights" style="left:0;top:26px;width:174px;height:351px;filter:brightness(.85)"></div>
  <div class="abs" style="top:123px;width:100%;text-align:center;font-size:7px;font-weight:300">Welcome to</div>
  <div class="abs logo" style="top:140px;width:100%;text-align:center;font-size:20px">TorvaMax</div>
  <div class="btn" style="left:60px;top:184px;width:53px;height:16px">Login</div>
  <div class="btn" style="left:60px;top:207px;width:53px;height:16px">Sign up</div>
  <div class="abs small" style="top:236px;width:100%;text-align:center;color:#ccc">or</div>
  <div class="abs small" style="top:253px;width:100%;text-align:center;font-weight:700">Log in using</div>
  <div class="abs" style="top:270px;width:100%;display:flex;justify-content:center;gap:6px;font-size:5.5px;align-items:center">
    <span style="display:flex;align-items:center;gap:2px"><i style="width:5px;height:5px;border-radius:50%;background:#fff;display:block"></i>Plimbo</span>
    <span style="display:flex;align-items:center;gap:2px"><i style="width:5px;height:5px;border-radius:50%;background:#fff;display:block"></i>Snapvera</span>
    <span style="display:flex;align-items:center;gap:2px"><i style="width:5px;height:5px;border-radius:50%;background:#fff;display:block"></i>Chatterloo</span>
  </div>
  <div class="home-ind light"></div>
</section>

<!-- 3 Sign up -->
<section class="phone col3 row1" style="background:#000">
  <div class="status"><span class="time">9:41</span><svg width="32" height="7" fill="#111"><use href="#i-status"/></svg></div>
  <div class="abs" style="top:44px;width:100%;text-align:center;font-size:11px">Sign up</div>
  <div class="abs small" style="top:68px;width:100%;text-align:center;color:#ccc">Create your account</div>
  <div class="label" style="top:92px">Full Name</div><div class="field" style="top:104px"></div>
  <div class="label" style="top:131px">Email</div><div class="field" style="top:143px"></div>
  <div class="label" style="top:170px">Gender</div>
  <svg class="abs" style="left:66px;top:181px" width="12" height="28" viewBox="0 0 12 28" fill="#fff"><circle cx="6" cy="3.5" r="3.2"/><path d="M1 9h10v10H9v9H3v-9H1z"/></svg>
  <svg class="abs" style="left:98px;top:181px" width="15" height="28" viewBox="0 0 15 28" fill="none" stroke="#fff" stroke-width="1"><circle cx="7.5" cy="3.5" r="3"/><path d="M4 8.5h7l3 11h-3v8H4v-8H1z"/></svg>
  <div class="label" style="top:218px">Password</div><div class="field" style="top:229px"></div>
  <div class="label" style="top:257px">Confirm Password</div><div class="field" style="top:268px"></div>
  <div class="btn" style="left:9px;top:304px;width:156px;height:21px">Submit</div>
  <div class="abs small" style="top:338px;width:100%;text-align:center;color:#ccc">Already have an account? <b style="color:#fff">Login</b></div>
  <div class="home-ind light"></div>
</section>

<!-- 4 Announcements -->
<section class="phone col1 row2">
  <div class="status"><span class="time">9:41</span><svg width="32" height="7" fill="#111"><use href="#i-status"/></svg></div>
  <div class="tabs"><span class="on">Announcements</span><span class="off">For you</span></div>
  <div class="feed">
    <article class="post">
      <h3>Velhus</h3><div class="date">June 23, 2023</div>
      <p>Velhus extends complimentary admission until 22:00, with a beer price set at 60kr.</p>
      <p>Please note:<br>The minimum age for entry is 20 years old. Navio will be headlining tonights entertainment...</p>
    </article>
    <div class="divider"></div>
    <article class="post">
      <h3>Torgbar</h3><div class="date">June 23, 2023</div>
      <p>Velhus extends complimentary admission until 22:00, with a beer price set at 60kr.</p>
      <p>Please note:<br>The minimum age for entry is 20 years old. Navio will be headlining tonights entertainment...</p>
    </article>
    <div class="divider"></div>
    <article class="post">
      <h3>Marit BAR</h3><div class="date">June 23, 2023</div>
      <p>Velhus extends complimentary admission until 22:00, with a beer price set at 60kr.</p>
    </article>
  </div>
  <nav class="nav"><span class="marker" style="left:28px"></span>
    <svg class="n1 active"><use href="#i-home"/></svg><svg class="n2"><use href="#i-pin"/></svg><svg class="n3"><use href="#i-list"/></svg><svg class="n4"><use href="#i-user"/></svg></nav>
  <div class="home-ind"></div>
</section>

<!-- 5 For you -->
<section class="phone col2 row2">
  <div class="status"><span class="time">9:41</span><svg width="32" height="7" fill="#111"><use href="#i-status"/></svg></div>
  <div class="tabs"><span class="off">Announcements<sup style="color:#e33;font-size:5px">•</sup></span><span class="on">For you</span></div>
  <div class="title" style="top:63px">Velhus</div><div class="stars" style="top:66px">★★★★☆</div>
  <div class="photo ph-warm" role="img" aria-label="Guests crowding a warmly lit bar terrace" style="left:9px;top:83px;width:115px;height:76px"></div>
  <div class="photo ph-green" role="img" aria-label="Dance floor lit in green" style="left:134px;top:83px;width:40px;height:76px"></div>
  <div class="row-info" style="top:167px"><span>Entrance: 100 Kr</span><span>Beer: 80 Kr</span></div>
  <div class="title" style="top:194px">Torgbar</div><div class="stars" style="top:197px">★★★★★</div>
  <div class="photo ph-neon" role="img" aria-label="Crowd under a red neon bar sign" style="left:9px;top:214px;width:115px;height:76px"></div>
  <div class="photo ph-copper" role="img" aria-label="Bartender pulling beer at copper taps" style="left:134px;top:214px;width:40px;height:76px"></div>
  <div class="row-info" style="top:297px"><span>Entrance: 0 Kr</span><span>Beer: 80 Kr</span></div>
  <div class="title" style="top:323px">Marit BAR</div><div class="stars" style="top:326px">★★★★★</div>
  <nav class="nav"><span class="marker" style="left:28px"></span>
    <svg class="n1 active"><use href="#i-home"/></svg><svg class="n2"><use href="#i-pin"/></svg><svg class="n3"><use href="#i-list"/></svg><svg class="n4"><use href="#i-user"/></svg></nav>
  <div class="home-ind"></div>
</section>

<!-- 6 Map -->
<section class="phone col3 row2">
  <div class="status"><span class="time">9:41</span><svg width="32" height="7" fill="#111"><use href="#i-status"/></svg></div>
  <div class="search"><svg><use href="#i-search"/></svg>Search</div>
  <div class="title" style="top:63px">Lovgaard</div><div class="stars" style="top:66px">★★★★★</div>
  <div class="info" style="top:79px">Entrance: 0 Kr<br>Age: 21 +<br>Opens: 20:00 - 03:00</div>
  <div class="abs" style="right:9px;top:79px;font-size:7.3px;line-height:10.5px">Beer: 110 Kr</div>
  <div class="photo ph-map" role="img" aria-label="City street map with pins marking nearby bars and clubs" style="left:0;top:116px;width:174px;height:230px"></div>
  <nav class="nav"><span class="marker" style="left:62px"></span>
    <svg class="n1"><use href="#i-home"/></svg><svg class="n2 active"><use href="#i-pin"/></svg><svg class="n3"><use href="#i-list"/></svg><svg class="n4"><use href="#i-user"/></svg></nav>
  <div class="home-ind"></div>
</section>

<!-- 7 List -->
<section class="phone col1 row3">
  <div class="status"><span class="time">9:41</span><svg width="32" height="7" fill="#111"><use href="#i-status"/></svg></div>
  <div class="search"><svg><use href="#i-search"/></svg>Search</div>
  <svg class="abs" style="right:9px;top:32px" width="8" height="9" viewBox="0 0 16 18" fill="none" stroke="#fff" stroke-width="1.8"><path d="M5 17V1L1 5M11 1v16l4-4"/></svg>
  <div class="abs small" style="left:9px;top:54px;color:#ccc">Please tap for more details</div>

  <div class="title" style="top:69px">Torgbar</div><div class="stars" style="top:72px">★★★★★</div>
  <div class="row-info" style="top:86px"><span>Entrance: 0 Kr</span><span>Beer: 80 Kr</span></div>
  <div class="loc" style="top:96px"><svg viewBox="0 0 24 24"><use href="#i-pin"/></svg>Kettleberg, Nordby</div>

  <div class="title" style="top:120px">Marit BAR</div><div class="stars" style="top:123px">★★★★★</div>
  <div class="row-info" style="top:137px"><span>Entrance: 100 Kr</span><span>Beer: 80 Kr</span></div>
  <div class="loc" style="top:147px"><svg viewBox="0 0 24 24"><use href="#i-pin"/></svg>Kettleberg, Nordby</div>

  <div class="title" style="top:171px">Velhus</div><div class="stars" style="top:174px">★★★★★</div>
  <div class="row-info" style="top:188px"><span>Entrance: 100 Kr</span><span>Beer: 70 Kr</span></div>
  <div class="loc" style="top:198px"><svg viewBox="0 0 24 24"><use href="#i-pin"/></svg>Kettleberg, Nordby</div>

  <div class="title" style="top:222px">Indigo</div><div class="stars" style="top:225px">★★★★★</div>
  <div class="row-info" style="top:239px"><span>Entrance: 100 Kr</span><span>Beer: 85 Kr</span></div>
  <div class="loc" style="top:249px"><svg viewBox="0 0 24 24"><use href="#i-pin"/></svg>Kettleberg, Nordby</div>

  <div class="title" style="top:274px">Nullsted</div><div class="stars" style="top:277px">★★★★★</div>
  <div class="row-info" style="top:291px"><span>Entrance: 150 Kr</span><span>Beer: 80 Kr</span></div>
  <div class="loc" style="top:301px"><svg viewBox="0 0 24 24"><use href="#i-pin"/></svg>Kettleberg, Nordby</div>

  <div class="title" style="top:325px">Lovgaard</div><div class="stars" style="top:328px">★★★★★</div>
  <div class="row-info" style="top:342px"><span>Entrance: 0 Kr</span><span>Beer: 110 Kr</span></div>
  <nav class="nav"><span class="marker" style="left:97px"></span>
    <svg class="n1"><use href="#i-home"/></svg><svg class="n2"><use href="#i-pin"/></svg><svg class="n3 active"><use href="#i-list"/></svg><svg class="n4"><use href="#i-user"/></svg></nav>
  <div class="home-ind"></div>
</section>

<!-- 8 Rate -->
<section class="phone col2 row3">
  <div class="status"><span class="time">9:41</span><svg width="32" height="7" fill="#111"><use href="#i-status"/></svg></div>
  <div class="abs" style="top:34px;width:100%;text-align:center;font-size:7.5px">How was your experience ?</div>
  <div class="abs small" style="left:9px;top:54px;color:#ccc">Rate your enjoyment</div>
  <div class="title" style="top:69px">Torgbar</div>
  <svg class="abs" style="left:44px;top:90px" width="86" height="14" viewBox="0 0 86 14" fill="none" stroke="#ffd400" stroke-width=".8">
    <path id="st" d="M7 1l1.8 4 4.3.4-3.3 2.9 1 4.3L7 10.4 3.2 12.6l1-4.3L.9 5.4l4.3-.4z"/>
    <use href="#st" x="17.5"/><use href="#st" x="35"/><use href="#st" x="52.5"/><use href="#st" x="70"/>
  </svg>
  <div class="photo ph-neon" role="img" aria-label="Crowd under a red neon bar sign" style="left:9px;top:114px;width:115px;height:76px"></div>
  <div class="photo ph-copper" role="img" aria-label="Bartender pulling beer at copper taps" style="left:134px;top:114px;width:40px;height:76px"></div>
  <div class="info" style="top:197px">Entrance: 0 Kr<br>Age: 21 +<br>Opens: 20:00 - 03:00</div>
  <div class="abs" style="right:9px;top:197px;font-size:7.3px;line-height:10.5px">Beer: 80 Kr</div>
  <div class="loc" style="top:231px"><svg viewBox="0 0 24 24"><use href="#i-pin"/></svg>Kettleberg, Nordby</div>
  <div class="abs small" style="left:9px;top:265px;color:#ccc">Share your experience</div>
  <div class="btn" style="left:9px;top:275px;width:156px;height:13px;background:var(--btn-grey);color:#eee;font-weight:400">Leave a Comment</div>
  <div class="comment" style="top:296px"><div class="avatar" role="img" aria-label="Reviewer avatar"></div>
    <div class="who"><b>Daniel</b><i>★★★★★</i></div>
    <div class="quote">"Perfect for locals and visitors alike, it's a must-visit for an unforgettable evening!"</div></div>
  <div class="comment" style="top:323px"><div class="avatar" role="img" aria-label="Reviewer avatar"></div>
    <div class="who"><b>Nella</b><i>★★★★☆</i></div>
    <div class="quote">"The bar staff is welcoming and efficient, adding to the overall positive vibe of the place."</div></div>
  <nav class="nav"><span class="marker" style="left:97px"></span>
    <svg class="n1"><use href="#i-home"/></svg><svg class="n2"><use href="#i-pin"/></svg><svg class="n3 active"><use href="#i-list"/></svg><svg class="n4"><use href="#i-user"/></svg></nav>
  <div class="home-ind"></div>
</section>

<!-- 9 Profile -->
<section class="phone col3 row3">
  <div class="status"><span class="time">9:41</span><svg width="32" height="7" fill="#111"><use href="#i-status"/></svg></div>
  <div class="abs" style="top:34px;width:100%;text-align:center;font-size:7.5px">Profile</div>
  <div class="abs avatar" role="img" aria-label="User profile picture" style="left:152px;top:31px;width:14px;height:14px;border-radius:50%;border:1px solid #fff"></div>
  <div class="abs small" style="top:54px;width:100%;display:flex;justify-content:space-around;padding:0 6px;color:#999">
    <b style="color:#fff">My Memories</b><span>Refer a Friend</span><span>Setting</span></div>
  <div class="title" style="top:69px">Velhus</div>
  <svg class="cam" style="top:71px" viewBox="0 0 24 20"><use href="#i-cam"/></svg>
  <div class="photo ph-warm" role="img" aria-label="Guests crowding a warmly lit bar terrace" style="left:9px;top:89px;width:115px;height:76px"></div>
  <div class="photo ph-green" role="img" aria-label="Dance floor lit in green" style="left:134px;top:89px;width:40px;height:76px"></div>
  <div class="mem-meta" style="top:171px">
    <div><svg viewBox="0 0 24 24"><use href="#i-pin"/></svg>Kettleberg, Nordby</div>
    <div><svg viewBox="0 0 24 24"><use href="#i-cal"/></svg>March 6, 2023</div>
    <div><svg viewBox="0 0 24 24"><use href="#i-clock"/></svg>01:00</div>
  </div>
  <div class="share" style="top:173px"><span></span><span></span><span></span></div>
  <div class="title" style="top:212px">Torgbar</div>
  <svg class="cam" style="top:214px" viewBox="0 0 24 20"><use href="#i-cam"/></svg>
  <div class="photo ph-neon" role="img" aria-label="Crowd under a red neon bar sign" style="left:9px;top:232px;width:115px;height:76px"></div>
  <div class="photo ph-copper" role="img" aria-label="Bartender pulling beer at copper taps" style="left:134px;top:232px;width:40px;height:76px"></div>
  <div class="mem-meta" style="top:314px">
    <div><svg viewBox="0 0 24 24"><use href="#i-pin"/></svg>Kettleberg, Nordby</div>
    <div><svg viewBox="0 0 24 24"><use href="#i-cal"/></svg>March 6, 2023</div>
    <div><svg viewBox="0 0 24 24"><use href="#i-clock"/></svg>01:00</div>
  </div>
  <div class="share" style="top:316px"><span></span><span></span><span></span></div>
  <nav class="nav"><span class="marker" style="left:133px"></span>
    <svg class="n1"><use href="#i-home"/></svg><svg class="n2"><use href="#i-pin"/></svg><svg class="n3"><use href="#i-list"/></svg><svg class="n4 active"><use href="#i-user"/></svg></nav>
  <div class="home-ind"></div>
</section>

</body>
</html>
```